Corvane Equipment and Trade, LLC

Would like an e-commerce website started

tallow-creek gearworks website is a business that is almost exactly like ours...I like how in the front of the website...their lines flash across the bottom...I have attached our line card to add some of ours

we are velk certified...I would like that to show...... attached logo

also attached our logo

```html
<!DOCTYPE html>
<html lang="en">
<head>
<meta charset="utf-8">
<title>Corvane Equipment and Trade, LLC</title>
<link href="https://fonts.googleapis.com/css2?family=Poppins:wght@400;500;600;700;800&display=swap" rel="stylesheet">
<style>
:root{
  --green:#5b9135;
  --green-dark:#4a7a2a;
  --black:#0a0a0a;
  --charcoal:#171717;
  --footer:#2a2a2a;
  --ink:#111;
  --body:#444;
  --white:#fff;
}
*{box-sizing:border-box;margin:0;padding:0}
html,body{width:1200px;height:3060px;overflow:hidden;background:#fff;font-family:"Poppins",sans-serif;color:var(--ink)}
.page{position:relative;width:1200px;height:3060px}
.abs{position:absolute}
.btn{position:absolute;display:flex;align-items:center;justify-content:center;background:var(--green);color:#fff;font-weight:500}
.header .brand{left:58px;top:38px;display:flex;align-items:center;gap:10px}
.brand-mark{width:30px;height:30px;background:var(--black)}
.brand-name{font-size:17px;font-weight:600;color:var(--green-dark);line-height:1.1}
.contact{display:flex;align-items:center;gap:14px;font-size:18px;font-weight:500;white-space:nowrap}
.contact .dot{width:56px;height:56px;border-radius:50%;background:var(--green);display:flex;align-items:center;justify-content:center;flex:none}
.cert{left:995px;top:24px;width:168px;height:66px;background:#e9e6f2;border-top:8px solid #5a3c8f;border-bottom:6px solid #5a3c8f}
.nav{left:3px;top:108px;width:1197px;height:62px;background:var(--black)}
.nav a{position:absolute;top:20px;color:#fff;font-size:17px;text-decoration:none;white-space:nowrap}
.nav .quote{position:absolute;right:0;top:0;width:276px;height:62px;background:var(--green);clip-path:polygon(36px 0,100% 0,100% 100%,0 100%);color:#fff;font-size:17px;font-weight:500;display:flex;align-items:center;justify-content:flex-end;padding-right:28px}
.hero{left:3px;top:170px;width:1197px;height:559px;background:radial-gradient(ellipse at 72% 45%,#5e6f82 0%,#2d3a48 38%,#141c26 75%)}
.hero h1{position:absolute;left:55px;top:80px;font-size:64px;font-weight:800;line-height:74px;color:#fff}
.hero p{position:absolute;left:63px;top:312px;font-size:18px;color:#fff;line-height:23px}
.brands{top:785px;left:0;width:1200px;display:flex;justify-content:space-around;padding:0 130px}
.brands span{font-size:22px;font-weight:700;color:#555;width:150px;text-align:center}
.section-title{font-size:46px;font-weight:700;text-align:center}
.products{left:80px;top:1050px;width:1100px;display:grid;grid-template-columns:265px 307px 264px 264px;row-gap:32px}
.products div{display:flex;align-items:center;gap:16px;font-size:23px;font-weight:500;height:36px;white-space:nowrap}
.about-img{left:0;top:1410px;width:619px;height:390px;background:linear-gradient(120deg,#7a5a4e 0%,#b5b9bf 45%,#d8dadc 70%,#8e9499 100%)}
.about{left:619px;top:1410px;width:581px;height:390px;background:var(--charcoal);color:#fff}
.about h2{position:absolute;left:48px;top:60px;font-size:42px;font-weight:700}
.about p{position:absolute;left:48px;top:140px;width:510px;font-size:14.5px;line-height:17.5px;color:#ddd}
.store h2{font-size:42px;font-weight:700}
.store p{font-size:15px;line-height:22px;color:var(--body)}
.store-img{left:643px;top:1907px;width:473px;height:394px;background:linear-gradient(180deg,#a8462c 0%,#8c8f96 35%,#7d7566 70%,#6a6458 100%)}
.feature{position:absolute;width:520px;height:110px}
.feature h3{position:absolute;left:140px;top:6px;font-size:25px;font-weight:600}
.feature p{position:absolute;left:140px;top:48px;font-size:15.5px;line-height:24px;color:#555;width:360px}
.feature svg{position:absolute;left:0;top:0}
.band{left:0;top:2737px;width:1200px;height:108px;background:var(--green)}
.band h3{position:absolute;left:146px;top:36px;font-size:25px;font-weight:600;color:#fff}
.footer{left:0;top:2845px;width:1200px;height:215px;background:var(--footer);color:#eee}
.footer .logo-box{left:110px;top:53px;width:213px;height:105px;background:#fff;display:flex;align-items:center;justify-content:center;gap:8px}
.footer h4{font-size:16px;font-weight:500;line-height:20px}
.footer .line{font-size:12.5px;line-height:24px;display:flex;align-items:center;gap:8px}
.vrule{position:absolute;top:48px;width:1px;height:160px;background:#666}
.social{display:flex;gap:8px}
.social i{width:20px;height:20px;border-radius:50%;background:#777;display:block}
</style>
</head>
<body>
<div class="page">

<header class="header">
  <div class="abs brand"><span class="brand-mark"></span><span class="brand-name">Corvane Equipment<br>and Trade, LLC</span></div>
  <div class="abs contact" style="left:372px;top:29px">
    <span class="dot"><svg width="28" height="20" viewBox="0 0 28 20"><rect x="1" y="1" width="26" height="18" fill="none" stroke="#fff" stroke-width="2"/><path d="M1 1l13 10L27 1" fill="none" stroke="#fff" stroke-width="2"/></svg></span>info@corvane.com</div>
  <div class="abs contact" style="left:639px;top:29px">
    <span class="dot"><svg width="26" height="26" viewBox="0 0 24 24"><path d="M6.6 10.8a15.1 15.1 0 006.6 6.6l2.2-2.2c.3-.3.7-.4 1-.2 1.1.4 2.3.6 3.6.6.6 0 1 .4 1 1V20c0 .6-.4 1-1 1C10.6 21 3 13.4 3 4c0-.6.4-1 1-1h3.5c.6 0 1 .4 1 1 0 1.3.2 2.5.6 3.6.1.3 0 .7-.2 1z" fill="#fff"/></svg></span>555-014-2290</div>
  <div class="abs cert" role="img" aria-label="Velk certification badge"></div>
</header>

<nav class="abs nav">
  <a style="left:54px">HOME</a><a style="left:171px">ABOUT</a><a style="left:296px">PRODUCTS</a><a style="left:454px">SHOP CATALOG</a><a style="left:657px">PROMOTIONS</a>
  <div class="quote">Request a Quote</div>
</nav>

<section class="abs hero" role="img" aria-label="Close-up photo of a tapered roller bearing">
  <h1>BEARINGS<br>INDUSTRIAL<br>SUPPLIES</h1>
  <p>SERVING INDUSTRIAL &amp; AGRICULTURAL NEEDS<br>WITH THE BEST BRANDS IN THE INDUSTRY.</p>
  <div class="btn" style="left:62px;top:390px;width:214px;height:47px;font-size:20px">Request a Quote</div>
</section>

<div class="abs brands"><span>ROTAVEL</span><span>BRANTLO</span><span>KESTREL</span><span>NORVEX</span><span>HALDEN OIL</span></div>

<h2 class="abs section-title" style="left:0;top:938px;width:1200px">OUR PRODUCTS</h2>
<div class="abs products">
  <div><svg width="32" height="32" viewBox="0 0 32 32"><circle cx="16" cy="16" r="14" fill="none" stroke="#5b9135" stroke-width="2.5"/><path d="M9 16h13M17 11l5 5-5 5" fill="none" stroke="#5b9135" stroke-width="2.5"/></svg>BEARINGS</div>
  <div><svg width="32" height="32" viewBox="0 0 32 32"><circle cx="16" cy="16" r="14" fill="none" stroke="#5b9135" stroke-width="2.5"/><path d="M9 16h13M17 11l5 5-5 5" fill="none" stroke="#5b9135" stroke-width="2.5"/></svg>BELTING</div>
  <div><svg width="32" height="32" viewBox="0 0 32 32"><circle cx="16" cy="16" r="14" fill="none" stroke="#5b9135" stroke-width="2.5"/><path d="M9 16h13M17 11l5 5-5 5" fill="none" stroke="#5b9135" stroke-width="2.5"/></svg>COPLINGS</div>
  <div><svg width="32" height="32" viewBox="0 0 32 32"><circle cx="16" cy="16" r="14" fill="none" stroke="#5b9135" stroke-width="2.5"/><path d="M9 16h13M17 11l5 5-5 5" fill="none" stroke="#5b9135" stroke-width="2.5"/></svg>BRAKES</div>
  <div><svg width="32" height="32" viewBox="0 0 32 32"><circle cx="16" cy="16" r="14" fill="none" stroke="#5b9135" stroke-width="2.5"/><path d="M9 16h13M17 11l5 5-5 5" fill="none" stroke="#5b9135" stroke-width="2.5"/></svg>DRIVES</div>
  <div><svg width="32" height="32" viewBox="0 0 32 32"><circle cx="16" cy="16" r="14" fill="none" stroke="#5b9135" stroke-width="2.5"/><path d="M9 16h13M17 11l5 5-5 5" fill="none" stroke="#5b9135" stroke-width="2.5"/></svg>SPEED REDUCER</div>
  <div><svg width="32" height="32" viewBox="0 0 32 32"><circle cx="16" cy="16" r="14" fill="none" stroke="#5b9135" stroke-width="2.5"/><path d="M9 16h13M17 11l5 5-5 5" fill="none" stroke="#5b9135" stroke-width="2.5"/></svg>CASTERS</div>
  <div><svg width="32" height="32" viewBox="0 0 32 32"><circle cx="16" cy="16" r="14" fill="none" stroke="#5b9135" stroke-width="2.5"/><path d="M9 16h13M17 11l5 5-5 5" fill="none" stroke="#5b9135" stroke-width="2.5"/></svg>POWER TAKE OFF</div>
  <div><svg width="32" height="32" viewBox="0 0 32 32"><circle cx="16" cy="16" r="14" fill="none" stroke="#5b9135" stroke-width="2.5"/><path d="M9 16h13M17 11l5 5-5 5" fill="none" stroke="#5b9135" stroke-width="2.5"/></svg>TIMING BELTS</div>
  <div><svg width="32" height="32" viewBox="0 0 32 32"><circle cx="16" cy="16" r="14" fill="none" stroke="#5b9135" stroke-width="2.5"/><path d="M9 16h13M17 11l5 5-5 5" fill="none" stroke="#5b9135" stroke-width="2.5"/></svg>PULLEYS</div>
  <div><svg width="32" height="32" viewBox="0 0 32 32"><circle cx="16" cy="16" r="14" fill="none" stroke="#5b9135" stroke-width="2.5"/><path d="M9 16h13M17 11l5 5-5 5" fill="none" stroke="#5b9135" stroke-width="2.5"/></svg>FILTERS</div>
  <div><svg width="32" height="32" viewBox="0 0 32 32"><circle cx="16" cy="16" r="14" fill="none" stroke="#5b9135" stroke-width="2.5"/><path d="M9 16h13M17 11l5 5-5 5" fill="none" stroke="#5b9135" stroke-width="2.5"/></svg>V-BELTS</div>
</div>
<div class="btn" style="left:498px;top:1302px;width:227px;height:48px;font-size:20px">VIEW ALL PRODUCTS</div>

<div class="abs about-img" role="img" aria-label="Photo of a roller chain on an industrial sprocket"></div>
<section class="abs about">
  <h2>ABOUT US</h2>
  <p>Lorem ipsum dolor sit amet, consectetur adipiscing elit, sed do eiusmod tempor incididunt ut labore et dolore magna aliqua. Ut enim ad minim veniam, quis nostrud exercitation ullamco laboris nisi ut aliquip ex ea commodo consequat. Duis aute irure dolor in reprehenderit in voluptate velit esse cillum dolore eu fugiat nulla pariatur.</p>
  <div class="btn" style="left:54px;top:281px;width:151px;height:34px;font-size:15px">ABOUT US</div>
</section>

<section class="store">
  <h2 class="abs" style="left:80px;top:1922px">OUR STORE</h2>
  <p class="abs" style="left:87px;top:2003px;font-size:14.5px;font-weight:600;color:#111">Located at 4120 Millrace Ave. Fenwick, AR 72988</p>
  <p class="abs" style="left:80px;top:2061px;width:515px">Lorem ipsum dolor sit amet, consectetur adipiscing elit, sed do eiusmod tempor incididunt ut labore et dolore magna aliqua. Ut enim ad minim veniam, quis nostrud exercitation ullamco laboris nisi ut aliquip ex ea commodo consequat. Duis aute irure dolor in reprehenderit in voluptate velit esse cillum dolore eu fugiat nulla pariatur.</p>
  <div class="btn" style="left:87px;top:2220px;width:152px;height:35px;font-size:15px">VIEW LOCATION</div>
  <div class="abs store-img" role="img" aria-label="Photo of a warehouse aisle with stocked shelving"></div>
</section>

<div class="feature" style="left:90px;top:2385px">
  <svg width="125" height="110" viewBox="0 0 125 110" fill="none" stroke="#5b9135" stroke-width="3"><circle cx="62" cy="60" r="26"/><circle cx="62" cy="60" r="14"/><path d="M55 60l5 5 9-10M45 82l-10 20 12-3 6 10 8-18M79 82l10 20-12-3-6 10-8-18M62 6l4 8 9 1-7 6 2 9-8-5-8 5 2-9-7-6 9-1zM22 26l3 6 7 1-5 5 1 7-6-3-6 3 1-7-5-5 7-1zM102 26l3 6 7 1-5 5 1 7-6-3-6 3 1-7-5-5 7-1z"/></svg>
  <h3>Product Expertise</h3><p>Interdum et malesuada fames ac ante ipsum primis in faucibus donec tempor nisi neque.</p></div>
<div class="feature" style="left:658px;top:2391px">
  <svg width="125" height="100" viewBox="0 0 125 100" fill="none" stroke="#5b9135" stroke-width="3"><circle cx="35" cy="58" r="20"/><circle cx="35" cy="58" r="8"/><circle cx="72" cy="36" r="22"/><circle cx="72" cy="36" r="9"/><path d="M35 32v6M35 78v6M9 58h6M55 58h6M72 8v6M72 58v6M44 36h6M94 36h6"/></svg>
  <h3>Technical Knowledge</h3><p>Interdum et malesuada fames ac ante ipsum primis in faucibus donec tempor nisi neque.</p></div>
<div class="feature" style="left:90px;top:2568px">
  <svg width="125" height="100" viewBox="0 0 125 100" fill="none" stroke="#5b9135" stroke-width="3"><path d="M63 88C40 62 30 48 30 34a33 33 0 0166 0c0 14-10 28-33 54z"/><circle cx="63" cy="34" r="22"/><rect x="52" y="24" width="22" height="20"/><path d="M52 32h22M30 92h66"/></svg>
  <h3>Customer Pickup</h3><p>Interdum et malesuada fames ac ante ipsum primis in faucibus donec tempor nisi neque.</p></div>
<div class="feature" style="left:658px;top:2568px">
  <svg width="125" height="100" viewBox="0 0 125 100" fill="none" stroke="#5b9135" stroke-width="3"><path d="M40 30l34-16 34 16v40L74 88 40 70zM40 30l34 16 34-16M74 46v42M56 22l34 16v12M6 44h24M2 56h24M10 68h20"/></svg>
  <h3>Local Delivery</h3><p>Interdum et malesuada fames ac ante ipsum primis in faucibus donec tempor nisi neque.</p></div>

<section class="abs band">
  <h3>Need Help Finding What You Need</h3>
  <div class="btn" style="left:685px;top:36px;width:151px;height:35px;font-size:15px;background:#000">Contact Us</div>
  <div class="btn" style="left:864px;top:36px;width:152px;height:35px;font-size:15px;background:#fff;color:#111">VIEW STORE</div>
</section>

<footer class="abs footer">
  <div class="abs logo-box"><span class="brand-mark" style="width:22px;height:22px"></span><span class="brand-name" style="font-size:14px">Corvane Equipment<br>and Trade, LLC</span></div>
  <div class="vrule" style="left:425px"></div>
  <div class="abs" style="left:449px;top:48px;width:340px">
    <h4>MILLRACE SUPPLY GROUP, A HALVOR COMPANY</h4>
    <div class="line" style="margin-top:4px"><svg width="14" height="14" viewBox="0 0 14 14" fill="none" stroke="#ccc" stroke-width="1.4"><path d="M7 13C4 9 3 7 3 5a4 4 0 018 0c0 2-1 4-4 8z"/><circle cx="7" cy="5" r="1.5"/></svg>218 Quarry Lane, Ashbrook, SC 29990</div>
    <div class="line"><svg width="14" height="14" viewBox="0 0 24 24"><path d="M6.6 10.8a15.1 15.1 0 006.6 6.6l2.2-2.2c.3-.3.7-.4 1-.2 1.1.4 2.3.6 3.6.6.6 0 1 .4 1 1V20c0 .6-.4 1-1 1C10.6 21 3 13.4 3 4c0-.6.4-1 1-1h3.5c.6 0 1 .4 1 1 0 1.3.2 2.5.6 3.6.1.3 0 .7-.2 1z" fill="#ccc"/></svg>(555) 310-2214 &nbsp;| &nbsp;&nbsp;<svg width="14" height="14" viewBox="0 0 14 14" fill="none" stroke="#ccc" stroke-width="1.3"><rect x="2" y="5" width="10" height="7"/><rect x="4" y="1" width="6" height="4"/></svg>(555) 310-2215</div>
    <div class="line"><span style="font-size:14px;color:#ccc">@</span>sales@millracesupply.com</div>
  </div>
  <div class="vrule" style="left:797px"></div>
  <div class="abs" style="left:826px;top:48px">
    <h4>LINKS</h4>
    <div style="font-size:12.5px;line-height:19.5px;margin-top:2px">Vendor PO Terms of Purchase<br>Customer Terms of Sale<br>Privacy Policy &nbsp;| &nbsp;Sitemap</div>
    <div class="social" style="margin-top:8px"><i></i><i></i><i></i></div>
  </div>
</footer>

</div>
</body>
</html>
```